International Trading Company, 'KIRO' needs a Business Card

The company name is "KIRO" and it has own logo design.
I'd like to use its logo on this business card.
I need two side Business Card.
I'll look forward to your great design.
Thank you very much in advance.

Contact Information for Business Card

Company Name : Kiro Harbour Limited
Information Example
Dorian Pallister
Mobile(use icon please) : 1 (212) 555-0143
Tel(use icon please) : 1 (212) 555-0178
Email(use icon please) : dorian27@kiroharbour-mail.com
Address(use icon please) : 482 Halden Ave, New York, NY 10160, USA

```html
<!DOCTYPE html>
<html lang="en">
<head>
<meta charset="utf-8">
<title>Kiro Harbour Limited – Business Card</title>
<link rel="stylesheet" href="https://fonts.googleapis.com/css2?family=Arimo:wght@700&family=PT+Sans:wght@400&display=swap">
<style>
  :root {
    --page-bg: #d8d6d4;
    --card-light: #eeebe9;
    --card-dark: #555557;
    --logo-grey: #4f4f51;
    --name-grey: #d6d6d8;
    --info-grey: #e4e4e6;
    --icon-grey: #dcdcde;
  }
  * { margin: 0; padding: 0; box-sizing: border-box; }
  html, body {
    width: 1200px;
    height: 900px;
    overflow: hidden;
    background: var(--page-bg);
  }
  .card {
    position: absolute;
    left: 150px;
    top: 171px;
    width: 900px;
    height: 558px;
    background: var(--card-light);
    overflow: hidden;
    box-shadow: 0 10px 30px rgba(0,0,0,0.18);
  }
  .card-panel {
    position: absolute;
    inset: 0;
    width: 900px;
    height: 558px;
  }
  .brand-name {
    position: absolute;
    right: 53px;
    top: 82px;
    font-family: "Arimo", Arial, sans-serif;
    font-weight: 700;
    font-size: 114px;
    line-height: 1;
    letter-spacing: 6px;
    color: var(--logo-grey);
  }
  .holder-name {
    position: absolute;
    left: 52px;
    top: 254px;
    font-family: "Arimo", Arial, sans-serif;
    font-weight: 700;
    font-size: 34px;
    letter-spacing: 0.5px;
    color: var(--name-grey);
    text-transform: uppercase;
  }
  .contact-list {
    position: absolute;
    left: 56px;
    top: 318px;
    list-style: none;
    font-family: "PT Sans", "Myriad Pro", sans-serif;
    font-size: 22px;
    color: var(--info-grey);
  }
  .contact-item {
    display: flex;
    align-items: center;
    height: 32.5px;
  }
  .contact-item.address { margin-top: 33px; }
  .contact-icon {
    width: 18px;
    height: 18px;
    margin-right: 12px;
    flex: none;
    fill: var(--icon-grey);
  }
</style>
</head>
<body>
  <article class="card" aria-label="Kiro Harbour Limited business card">
    <svg class="card-panel" viewBox="0 0 900 558" aria-hidden="true">
      <polygon points="0,0 324,0 682,558 0,558" fill="var(--card-dark)"/>
    </svg>

    <div class="brand-name">KIRO</div>

    <h1 class="holder-name">Dorian Pallister</h1>

    <ul class="contact-list">
      <li class="contact-item">
        <svg class="contact-icon" viewBox="0 0 18 18" aria-label="Mobile"><path d="M5 1h8a1 1 0 0 1 1 1v14a1 1 0 0 1-1 1H5a1 1 0 0 1-1-1V2a1 1 0 0 1 1-1zm1 2v10h6V3zm3 11.2a1 1 0 1 0 0 2 1 1 0 0 0 0-2z"/></svg>
        <span>1 (212) 555-0143</span>
      </li>
      <li class="contact-item">
        <svg class="contact-icon" viewBox="0 0 18 18" aria-label="Telephone"><path d="M2 6c0-2 3-3 7-3s7 1 7 3v1.5h-3.5V6h-7v1.5H2zM5 8h8l2.5 4v3.5h-13V12zm4 1.6a2 2 0 1 0 0 4 2 2 0 0 0 0-4z"/></svg>
        <span>1 (212) 555-0178</span>
      </li>
      <li class="contact-item">
        <svg class="contact-icon" viewBox="0 0 18 18" aria-label="Website"><circle cx="9" cy="9" r="8"/><path d="M4 6c2 0 3 1 2.5 3s1.5 2 1.5 4l-1 2.5M12 3.5c-1 1.5 0 2.5 1.5 2.5s1.5 2 .5 3.5" stroke="var(--card-dark)" stroke-width="1.6" fill="none"/></svg>
        <span>www.kiroharbour.com</span>
      </li>
      <li class="contact-item">
        <svg class="contact-icon" viewBox="0 0 18 18" aria-label="Email"><path d="M1.5 4h15v10h-15z"/><path d="M1.5 4.5 9 10l7.5-5.5" stroke="var(--card-dark)" stroke-width="1.4" fill="none"/></svg>
        <span>dorian27@kiroharbour-mail.com</span>
      </li>
      <li class="contact-item address">
        <svg class="contact-icon" viewBox="0 0 18 18" aria-label="Address"><path d="M9 1a6 6 0 0 1 6 6c0 4.5-6 10-6 10S3 11.5 3 7a6 6 0 0 1 6-6zm0 3.5a2.5 2.5 0 1 0 0 5 2.5 2.5 0 0 0 0-5z"/></svg>
        <span>482 Halden Ave, New York, NY 10160, USA</span>
      </li>
    </ul>
  </article>
</body>
</html>
```